Halden & Pruitt Periodontics and Implant Solutions Business Card

We are a specialty dental practice- implants and periodontal surgery. We have just re-designed our logo and are building a new office and would like to re-design our business card. We are looking for something professional with a creative and artsy twist- something to stand out among the rest! Happy Designing!

I have uploaded all versions of our new logo and our current business card. We have 3 locations and 2 doctors.

Target Market(s)

55+

Industry/Entity Type

Dental

Contact Information for Business Card

Needs Names, logo, locations- professional and artsy!

Colors
0555a3
0592cd
34a7d7
3277b5
85cae6
85acd3
cee9f5
ecf7fb

Requirements
Must have
• our names:
• Thomas E. Halden D.M.D.
• Celia M. Pruitt D.M.D.
• Diplomate of the National Council of Gum Surgery
• Address locations:
• 462 W. Larkspur Avenue Suite 210B Plantation, FL 33871
• Tel: 954-318-2264 Fax: 954-318-2291
• 5127 Harlow Lane #C-4 Boca Raton, FL 33609
• Tel: 561-627-1958 Fax: 561-703-2816
• 274 Northwest 9th Street #412 Miami FL 33987
• Tel: 786-429-6153 Fax: 786-429-6170
Nice to have
• unique look
Should not have
• doesn't need QR like our current card has.

```html
<!DOCTYPE html>
<html lang="en">
<head>
<meta charset="UTF-8">
<title>Halden &amp; Pruitt Business Card</title>
<link rel="stylesheet" href="https://fonts.googleapis.com/css2?family=Open+Sans:wght@400;600;700&display=swap">
<style>
  :root {
    --backdrop: #d9d6d2;
    --card-black: #0b0b0c;
    --card-edge: #1c1c1e;
    --brand-blue: #2f4ea8;
    --icon-blue: #3277b5;
    --ink-white: #f2f2f2;
    --silver: #c9cacc;
  }
  * { box-sizing: border-box; margin: 0; padding: 0; }
  html, body {
    width: 1200px; height: 900px; overflow: hidden;
    background: var(--backdrop);
    font-family: "Open Sans", Arial, sans-serif;
  }
  .stage { position: relative; width: 1200px; height: 900px; }
  .card {
    position: absolute; top: 296px;
    width: 540px; height: 308px;
    background: var(--card-black);
    border: 1px solid var(--card-edge);
    box-shadow: 0 10px 28px rgba(0,0,0,0.35);
    color: var(--ink-white);
  }
  .card--front { left: 40px; }
  .card--back { left: 620px; }

  .brand {
    position: absolute; display: flex; flex-direction: column;
    align-items: center; text-align: center;
  }
  .brand__circle {
    width: 124px; height: 124px; border-radius: 50%;
    border: 6px solid var(--silver);
  }
  .brand__name {
    margin-top: 10px; width: 190px;
    font-size: 12px; font-weight: 600; line-height: 1.3;
    color: var(--silver);
  }
  .card--front .brand { left: 34px; top: 70px; }
  .card--back .brand { left: 28px; top: 70px; }

  .divider {
    position: absolute; left: 246px; top: 58px;
    width: 1px; height: 190px; background: var(--brand-blue);
  }
  .doctors { position: absolute; left: 266px; top: 62px; }
  .doctors__name {
    font-size: 19px; font-weight: 700; line-height: 1.2;
    color: var(--brand-blue);
  }
  .doctors__title {
    margin-top: 4px; font-size: 13.5px; line-height: 1.45;
  }
  .contact-list { position: absolute; left: 266px; top: 196px; list-style: none; }
  .contact-list li {
    display: flex; align-items: center; gap: 8px;
    font-size: 13.5px; line-height: 1.7;
  }
  .icon { width: 11px; height: 11px; fill: var(--icon-blue); flex: none; }

  .locations { position: absolute; left: 258px; top: 26px; width: 270px; }
  .location { margin-bottom: 18px; font-size: 12.5px; line-height: 1.4; }
  .location__row { display: flex; align-items: flex-start; gap: 8px; }
  .location__row .icon { margin-top: 3px; }
  .location__phones { display: flex; gap: 22px; }
  .location__phones span { display: flex; align-items: center; gap: 8px; }
</style>
</head>
<body>
<div class="stage">

  <section class="card card--front" aria-label="Card front">
    <div class="brand">
      <div class="brand__circle"></div>
      <p class="brand__name">Halden &amp; Pruitt Periodontics and Implant Solutions</p>
    </div>
    <div class="divider"></div>
    <div class="doctors">
      <p class="doctors__name">Thomas E. Halden D.M.D.</p>
      <p class="doctors__name">Celia M. Pruitt D.M.D.</p>
      <p class="doctors__title">Diplomate of the National<br>Council of Gum Surgery</p>
    </div>
    <ul class="contact-list">
      <li>
        <svg class="icon" viewBox="0 0 12 12"><path d="M0 2h12v8H0z M0 2l6 4 6-4" fill="var(--icon-blue)"/></svg>
        contactus@haldenperio.com
      </li>
      <li>
        <svg class="icon" viewBox="0 0 12 12"><circle cx="6" cy="6" r="5.5"/><path d="M0.5 6h11M6 0.5v11" stroke="#0b0b0c" stroke-width="1"/></svg>
        www.haldenperio.com
      </li>
    </ul>
  </section>

  <section class="card card--back" aria-label="Card back">
    <div class="brand">
      <div class="brand__circle"></div>
      <p class="brand__name">Halden &amp; Pruitt Periodontics and Implant Solutions</p>
    </div>
    <div class="locations">
      <div class="location">
        <div class="location__row">
          <svg class="icon" viewBox="0 0 12 12"><path d="M6 0a4 4 0 0 1 4 4c0 3-4 8-4 8S2 7 2 4a4 4 0 0 1 4-4z"/></svg>
          <span>462 W. Larkspur Avenue Suite<br>210B Plantation, FL 33871</span>
        </div>
        <div class="location__phones">
          <span><svg class="icon" viewBox="0 0 12 12"><path d="M2 0l3 3-1.5 1.5a7 7 0 0 0 4 4L9 7l3 3-2 2C5 12 0 7 0 2z"/></svg>954-318-2264</span>
          <span><svg class="icon" viewBox="0 0 12 12"><path d="M3 0h6v4H3zM0 4h12v6H0zM3 8h6v4H3z"/></svg>954-318-2291</span>
        </div>
      </div>
      <div class="location">
        <div class="location__row">
          <svg class="icon" viewBox="0 0 12 12"><path d="M6 0a4 4 0 0 1 4 4c0 3-4 8-4 8S2 7 2 4a4 4 0 0 1 4-4z"/></svg>
          <span>5127 Harlow Lane #C-4<br>Boca Raton, FL 33609</span>
        </div>
        <div class="location__phones">
          <span><svg class="icon" viewBox="0 0 12 12"><path d="M2 0l3 3-1.5 1.5a7 7 0 0 0 4 4L9 7l3 3-2 2C5 12 0 7 0 2z"/></svg>561-627-1958</span>
          <span><svg class="icon" viewBox="0 0 12 12"><path d="M3 0h6v4H3zM0 4h12v6H0zM3 8h6v4H3z"/></svg>561-703-2816</span>
        </div>
      </div>
      <div class="location">
        <div class="location__row">
          <svg class="icon" viewBox="0 0 12 12"><path d="M6 0a4 4 0 0 1 4 4c0 3-4 8-4 8S2 7 2 4a4 4 0 0 1 4-4z"/></svg>
          <span>274 Northwest 9th Street<br>#412 Miami FL 33987</span>
        </div>
        <div class="location__phones">
          <span><svg class="icon" viewBox="0 0 12 12"><path d="M2 0l3 3-1.5 1.5a7 7 0 0 0 4 4L9 7l3 3-2 2C5 12 0 7 0 2z"/></svg>786-429-6153</span>
          <span><svg class="icon" viewBox="0 0 12 12"><path d="M3 0h6v4H3zM0 4h12v6H0zM3 8h6v4H3z"/></svg>786-429-6170</span>
        </div>
      </div>
    </div>
  </section>

</div>
</body>
</html>
```